Nachtfunke - needs a CD/Cover Design for a VA Compilation

We need a CD-Design/Cover-Artwork for our Various Artists Compilation called 'Nachtfunke', which means "Night spark". Back then our events were based in one of Germanys best underground techno-clubs., which we also called "our temple".
The artists featured on this compilation rather performed at our events or had a massive influence on the music the djs played.
The sound is glitchy, technically detailed and a little unpredictable.

We would like to see some designs not too colourful!

Target Market(s)

complex electronic music listeners

Industry/Entity Type

Club

Font styles to use
Sans Serif

Colors
ec1f27

Requirements
Must have
• Ideally the artwork should be something otherworldly, abstract/glitchy, be an optical illusion and/or have geometric complexity.
Nice to have
• - probably black and white design fits better with us, but you can also try it with a very few colors.
- maybe something futuristic or scatchy
Should not have
• - it should definitely NOT be too colourful.
- no humans!! or animals
- in case you think to draw a temple, please use it more abstract, nothing too obviously, we dont wanna look like a hippie event!
- no musical notes
- no obvious "play" symbol / headphones or vinyl images

```html
<!DOCTYPE html>
<html lang="de">
<head>
<meta charset="utf-8">
<title>Nachtfunke – VA Compilation Cover</title>
<link rel="stylesheet" href="https://fonts.googleapis.com/css2?family=Exo+2:ital,wght@1,800&display=swap">
<style>
  :root {
    --page-bg: #f4f4f4;
    --title-red: #e0505e;
    --title-shadow: #2b2b33;
    --title-cyan: #3fd6d0;
    --glitch-magenta: #d64fc8;
    --glitch-green: #4fe07a;
    --glitch-yellow: #e8dc5a;
    --glitch-cyan: #52e0e6;
    --glitch-red: #e0505e;
    --glitch-white: #f2f0f0;
    --vault-light: #ebe9e9;
    --vault-mid: #a3a1a1;
    --vault-dark: #404040;
    --vault-deep: #2e2e2e;
  }
  * { margin: 0; padding: 0; box-sizing: border-box; }
  html, body {
    width: 1200px;
    height: 1000px;
    overflow: hidden;
    background: var(--page-bg);
  }
  .cover {
    position: absolute;
    left: 172px;
    top: 64px;
    width: 868px;
    height: 868px;
    overflow: hidden;
  }
  .cover-artwork {
    position: absolute;
    inset: 0;
    background:
      radial-gradient(ellipse 20% 16% at 50% 46%, rgba(120,200,190,0.45) 0%, rgba(120,200,190,0) 100%),
      radial-gradient(ellipse 34% 30% at 50% 44%, var(--vault-light) 0%, rgba(235,233,233,0.85) 45%, rgba(235,233,233,0) 100%),
      radial-gradient(ellipse 26% 18% at 50% 72%, rgba(210,190,215,0.7) 0%, rgba(210,190,215,0) 100%),
      linear-gradient(180deg, rgba(60,60,60,0) 0%, rgba(60,60,60,0) 62%, rgba(46,46,46,0.55) 100%),
      radial-gradient(ellipse 72% 68% at 50% 42%, var(--vault-mid) 0%, var(--vault-dark) 80%, var(--vault-deep) 100%);
  }
  .glitch-bands {
    position: absolute;
    inset: 0;
  }
  .cover-title {
    position: absolute;
    inset: 0;
    width: 868px;
    height: 868px;
  }
  .cover-title text {
    font-family: 'Exo 2', sans-serif;
    font-style: italic;
    font-weight: 800;
    font-size: 150px;
  }
  .title-shadow { fill: var(--title-shadow); }
  .title-cyan { fill: var(--title-cyan); opacity: 0.7; }
  .title-main { fill: var(--title-red); }
</style>
</head>
<body>
  <main class="cover">
    <div class="cover-artwork" role="img" aria-label="Glitched black-and-white photograph of a vaulted cloister corridor with stone arches, split by RGB colour offsets"></div>

    <svg class="glitch-bands" viewBox="0 0 868 868" aria-hidden="true">
      <!-- vertical channel streaks -->
      <rect x="150" y="120" width="6" height="560" fill="var(--glitch-magenta)" opacity="0.22"/>
      <rect x="210" y="200" width="4" height="480" fill="var(--glitch-green)" opacity="0.22"/>
      <rect x="648" y="200" width="5" height="480" fill="var(--glitch-yellow)" opacity="0.25"/>
      <rect x="712" y="120" width="6" height="560" fill="var(--glitch-cyan)" opacity="0.22"/>
      <rect x="330" y="150" width="4" height="300" fill="var(--glitch-magenta)" opacity="0.25"/>
      <rect x="534" y="150" width="4" height="300" fill="var(--glitch-green)" opacity="0.25"/>

      <!-- upper slices -->
      <rect x="0" y="205" width="120" height="20" fill="var(--glitch-magenta)" opacity="0.2"/>
      <rect x="600" y="205" width="100" height="20" fill="var(--glitch-yellow)" opacity="0.25"/>
      <rect x="0" y="265" width="868" height="20" fill="var(--glitch-white)" opacity="0.2"/>
      <rect x="0" y="265" width="90" height="20" fill="var(--glitch-magenta)" opacity="0.25"/>
      <rect x="790" y="265" width="78" height="20" fill="var(--glitch-yellow)" opacity="0.35"/>
      <rect x="80" y="320" width="620" height="20" fill="var(--glitch-white)" opacity="0.3"/>
      <rect x="220" y="375" width="648" height="20" fill="var(--glitch-white)" opacity="0.3"/>
      <rect x="780" y="375" width="50" height="20" fill="var(--glitch-cyan)" opacity="0.35"/>
      <rect x="420" y="395" width="60" height="14" fill="var(--glitch-red)" opacity="0.35"/>

      <!-- title floor band -->
      <rect x="0" y="515" width="868" height="20" fill="var(--glitch-white)" opacity="0.4"/>
      <rect x="0" y="535" width="868" height="40" fill="var(--glitch-white)" opacity="0.15"/>

      <!-- main glitch row -->
      <rect x="124" y="650" width="56" height="42" fill="var(--glitch-green)" opacity="0.55"/>
      <rect x="180" y="650" width="20" height="42" fill="var(--glitch-cyan)" opacity="0.6"/>
      <rect x="200" y="650" width="90" height="42" fill="var(--glitch-white)" opacity="0.55"/>
      <rect x="290" y="650" width="110" height="42" fill="var(--glitch-magenta)" opacity="0.35"/>
      <rect x="400" y="650" width="160" height="42" fill="var(--glitch-cyan)" opacity="0.4"/>
      <rect x="450" y="650" width="50" height="22" fill="var(--glitch-red)" opacity="0.4"/>
      <rect x="560" y="650" width="80" height="42" fill="var(--glitch-magenta)" opacity="0.4"/>
      <rect x="640" y="650" width="120" height="42" fill="var(--glitch-yellow)" opacity="0.35"/>

      <!-- lower slices -->
      <rect x="170" y="795" width="90" height="20" fill="var(--glitch-magenta)" opacity="0.35"/>
      <rect x="260" y="795" width="70" height="20" fill="var(--glitch-green)" opacity="0.35"/>
      <rect x="560" y="795" width="80" height="20" fill="var(--glitch-red)" opacity="0.35"/>
      <rect x="650" y="795" width="50" height="20" fill="var(--glitch-cyan)" opacity="0.35"/>
    </svg>

    <svg class="cover-title" viewBox="0 0 868 868">
      <defs>
        <clipPath id="title-upper-slice"><rect x="0" y="0" width="868" height="548"/></clipPath>
        <clipPath id="title-lower-slice"><rect x="0" y="548" width="868" height="320"/></clipPath>
      </defs>
      <g clip-path="url(#title-upper-slice)">
        <text class="title-shadow" x="52" y="532" textLength="770" lengthAdjust="spacingAndGlyphs" aria-hidden="true">NACHTFUNKE</text>
        <text class="title-cyan" x="36" y="522" textLength="770" lengthAdjust="spacingAndGlyphs" aria-hidden="true">NACHTFUNKE</text>
        <text class="title-main" x="44" y="526" textLength="770" lengthAdjust="spacingAndGlyphs">NACHTFUNKE</text>
      </g>
      <g clip-path="url(#title-lower-slice)" aria-hidden="true">
        <text class="title-shadow" x="64" y="532" textLength="770" lengthAdjust="spacingAndGlyphs">NACHTFUNKE</text>
        <text class="title-cyan" x="48" y="522" textLength="770" lengthAdjust="spacingAndGlyphs">NACHTFUNKE</text>
        <text class="title-main" x="56" y="526" textLength="770" lengthAdjust="spacingAndGlyphs">NACHTFUNKE</text>
      </g>
    </svg>
  </main>
</body>
</html>
```